Tolvar Mechanical Services Cultural Norms

Tale the uploaded list of cultural norms and develop a design that showcases how these 8 items encompass everything about our companies culture.

```html
<!DOCTYPE html>
<html lang="en">
<head>
<meta charset="utf-8">
<title>Tolvar Mechanical Services – Cultural Norms</title>
<link rel="stylesheet" href="https://fonts.googleapis.com/css2?family=Oswald:wght@500;600;700&family=Arimo:wght@400;700&display=swap">
<style>
  :root{
    --backdrop:#3a322d;
    --gold:#8a7048;
    --paper:#ede8e3;
    --ink:#0d0d0d;
    --white:#ffffff;
    --body:#1d1d1d;
  }
  *{margin:0;padding:0;box-sizing:border-box}
  html,body{width:1200px;height:1200px;overflow:hidden;background:var(--backdrop)}
  .canvas{position:relative;width:1200px;height:1200px}
  .sheet{position:absolute;left:213px;top:57px;width:773px;height:1085px;background:var(--paper);overflow:hidden}
  .hero-photo{position:absolute;left:0;top:0;width:773px;height:350px;
    background:linear-gradient(100deg,#f4f3f3 0%,#e4e2e3 35%,#9a948f 58%,#6f6a5a 78%,#a79a9a 100%)}
  .hero-band{position:absolute;left:0;top:350px;width:773px;height:14px;background:var(--gold)}
  .brand-mark{position:absolute;left:24px;top:27px;width:66px;height:66px;background:var(--ink)}
  .brand-name{position:absolute;left:104px;top:18px;font-family:'Oswald',sans-serif;font-weight:600;color:var(--gold);line-height:1;white-space:nowrap}
  .brand-name .first{display:block;font-size:52px;letter-spacing:6px}
  .brand-name .second{display:block;font-size:26px;letter-spacing:2.6px;margin-top:3px}
  .tagline{position:absolute;left:25px;top:101px;font-family:'Arimo',sans-serif;font-weight:700;font-size:11.5px;letter-spacing:3.4px;color:var(--gold);white-space:nowrap}
  .norms-art{position:absolute;left:0;top:0}
  .title{position:absolute;left:23px;font-family:'Oswald',sans-serif;font-weight:700;line-height:1;letter-spacing:.5px}
  .title-top{top:638px;font-size:48px;color:var(--gold)}
  .title-bottom{top:690px;font-size:62px;color:var(--ink)}
  .norm{position:absolute;right:23px}
  .norm h2{font-family:'Oswald',sans-serif;font-weight:600;font-size:19px;line-height:24px;color:var(--gold);
    padding-bottom:4px;border-bottom:1px dashed #8c8c8c;margin-left:-18px;padding-left:18px;width:80%}
  .norm p{font-family:'Arimo',sans-serif;font-size:13.6px;line-height:18px;color:var(--body);text-align:justify;margin-top:5px}
  .footer-bar{position:absolute;left:0;top:1061px;width:773px;height:24px;background:var(--ink)}
  .footer-accent{position:absolute;left:0;top:0}
</style>
</head>
<body>
<div class="canvas">
  <div class="sheet">
    <div class="hero-photo" role="img" aria-label="Photo of a company service van with roof ladders driving along a tree-lined road"></div>
    <div class="brand-mark"></div>
    <div class="brand-name"><span class="first">TOLVAR</span><span class="second">MECHANICAL SERVICES</span></div>
    <div class="tagline">COMFORT YOU CAN COUNT ON, EVERY DAY</div>
    <div class="hero-band"></div>

    <svg class="norms-art" width="773" height="1085" viewBox="0 0 773 1085">
      <defs>
        <clipPath id="below-band"><rect x="0" y="364" width="773" height="697"/></clipPath>
      </defs>
      <g clip-path="url(#below-band)">
        <circle cx="-43" cy="711" r="329" fill="var(--white)"/>
        <circle cx="-43" cy="711" r="333" fill="none" stroke="var(--ink)" stroke-width="9"/>
        <circle cx="-43" cy="711" r="318" fill="none" stroke="var(--gold)" stroke-width="2.5"/>
      </g>
      <g fill="var(--white)" stroke="#b9a887" stroke-width="1">
        <path d="M99 394 h40 a21 21 0 0 1 0 42 h-40 z"/>
        <path d="M195 462 h40 a21 21 0 0 1 0 42 h-40 z"/>
        <path d="M254 551 h40 a21 21 0 0 1 0 42 h-40 z"/>
        <path d="M282 641 h40 a21 21 0 0 1 0 42 h-40 z"/>
        <path d="M282 737 h40 a21 21 0 0 1 0 42 h-40 z"/>
        <path d="M255 830 h40 a21 21 0 0 1 0 42 h-40 z"/>
        <path d="M194 917 h40 a21 21 0 0 1 0 42 h-40 z"/>
        <path d="M99 987 h40 a21 21 0 0 1 0 42 h-40 z"/>
      </g>
      <g font-family="Oswald, sans-serif" font-weight="700" font-size="30" fill="var(--ink)">
        <text x="150" y="427">1.</text>
        <text x="246" y="495">2.</text>
        <text x="305" y="584">3.</text>
        <text x="333" y="674">4.</text>
        <text x="333" y="770">5.</text>
        <text x="306" y="863">6.</text>
        <text x="245" y="950">7.</text>
        <text x="150" y="1020">8.</text>
      </g>
      <g>
        <g transform="translate(99 415)"><circle r="42" fill="var(--gold)"/><circle r="30" fill="var(--ink)" stroke="var(--white)" stroke-width="2.5"/>
          <g stroke="var(--white)" stroke-width="2.5" fill="none"><path d="M-20 -4 a20 20 0 0 1 34 -12"/><path d="M20 4 a20 20 0 0 1 -34 12"/><path d="M-8 10 v-12 M0 10 v-18 M8 10 v-14"/><path d="M-11 -1 l3 -3 3 3 M-3 -7 l3 -3 3 3 M5 -3 l3 -3 3 3"/><path d="M-12 11 h24"/></g></g>
        <g transform="translate(195 483)"><circle r="42" fill="var(--gold)"/><circle r="30" fill="var(--ink)" stroke="var(--white)" stroke-width="2.5"/>
          <g fill="var(--white)"><path d="M-12 -14 l2 4 4 0 -3 3 1 4 -4 -2 -4 2 1 -4 -3 -3 4 0z"/><path d="M0 -17 l2 4 4 0 -3 3 1 4 -4 -2 -4 2 1 -4 -3 -3 4 0z"/><path d="M12 -14 l2 4 4 0 -3 3 1 4 -4 -2 -4 2 1 -4 -3 -3 4 0z"/>
          <circle cx="-11" cy="3" r="3.5"/><circle cx="11" cy="3" r="3.5"/><circle cx="0" cy="2" r="4.5"/><path d="M-18 15 a7 7 0 0 1 14 0z M4 15 a7 7 0 0 1 14 0z M-8 16 a8 8 0 0 1 16 0z"/></g></g>
        <g transform="translate(254 572)"><circle r="42" fill="var(--gold)"/><circle r="30" fill="var(--ink)" stroke="var(--white)" stroke-width="2.5"/>
          <g fill="var(--white)"><circle cx="0" cy="-14" r="5"/><path d="M-14 -18 l6 10 h16 l6 -10 3 2 -8 14 h-18 l-8 -14z"/><rect x="-10" y="5" width="20" height="13" rx="2"/></g></g>
        <g transform="translate(282 662)"><circle r="42" fill="var(--gold)"/><circle r="30" fill="var(--ink)" stroke="var(--white)" stroke-width="2.5"/>
          <g fill="var(--white)"><rect x="-12" y="-19" width="18" height="13" rx="3"/><path d="M-8 -6 l-2 5 6 -5z"/><circle cx="-8" cy="3" r="4"/><circle cx="8" cy="-3" r="4"/><path d="M-16 17 a8 8 0 0 1 16 0z M0 13 a8 8 0 0 1 16 0 v4 h-16z"/></g>
          <path d="M-7 -13 l2 2 5 -5" stroke="var(--ink)" stroke-width="2" fill="none"/></g>
        <g transform="translate(282 758)"><circle r="42" fill="var(--gold)"/><circle r="30" fill="var(--ink)" stroke="var(--white)" stroke-width="2.5"/>
          <g fill="var(--white)"><circle cx="7" cy="-9" r="7"/><path d="M-20 4 l8 -3 h10 l-2 4 h-6 h10 l14 -6 2 3 -16 10 h-14 l-4 3z"/></g><circle cx="7" cy="-9" r="3" fill="var(--ink)"/></g>
        <g transform="translate(255 851)"><circle r="42" fill="var(--gold)"/><circle r="30" fill="var(--ink)" stroke="var(--white)" stroke-width="2.5"/>
          <g fill="var(--white)"><path d="M-16 18 v-6 h7 v-6 h7 v-6 h7 v-6 h9 v3 h-6 v6 h-7 v6 h-7 v6 h-7 v3z"/><circle cx="-8" cy="-17" r="3.5"/><path d="M-11 -12 h6 l2 10 -3 0 -1 8 -3 0z"/></g></g>
        <g transform="translate(194 938)"><circle r="42" fill="var(--gold)"/><circle r="30" fill="var(--ink)" stroke="var(--white)" stroke-width="2.5"/>
          <g fill="none" stroke="var(--white)" stroke-width="2.5" stroke-linejoin="round"><path d="M-20 -6 l8 -6 8 4 8 -4 8 6"/><path d="M-14 -2 l12 12 4 -3 -10 -10"/><path d="M14 -2 l-10 10 M-2 -4 l8 -4 10 10"/></g></g>
        <g transform="translate(99 1008)"><circle r="42" fill="var(--gold)"/><circle r="30" fill="var(--ink)" stroke="var(--white)" stroke-width="2.5"/>
          <g fill="var(--white)"><circle cx="0" cy="-4" r="13"/><path d="M-8 6 l-5 14 5 -3 3 4 4 -10z M8 6 l5 14 -5 -3 -3 4 -4 -10z"/></g>
          <circle cx="0" cy="-4" r="8" fill="var(--ink)"/><path d="M0 -9 l1.5 3.5 3.7 0 -3 2.3 1.2 3.6 -3.4 -2.2 -3.4 2.2 1.2 -3.6 -3 -2.3 3.7 0z" fill="var(--white)"/></g>
      </g>
    </svg>

    <div class="title title-top">CULTURAL</div>
    <div class="title title-bottom">NORMS</div>

    <div class="norm" style="left:204px;top:388px">
      <h2>Continuous Improvement:</h2>
      <p>We believe that there is always room for improvement in everything we do.</p>
    </div>
    <div class="norm" style="left:297px;top:456px">
      <h2>Enhancing Lives:</h2>
      <p>Our aim is to positively impact the lives of others through our actions and services.</p>
    </div>
    <div class="norm" style="left:357px;top:544px">
      <h2>Cultivating Encouragement:</h2>
      <p>We believe that fostering encouragement among our team members leads to personal fulfillment and opportunity.</p>
    </div>
    <div class="norm" style="left:384px;top:635px">
      <h2>Effective Communication:</h2>
      <p>We embrace the challenge of effective communication, recognizing its importance in our success.</p>
    </div>
    <div class="norm" style="left:384px;top:731px">
      <h2>Think. Act. Take Ownership:</h2>
      <p>We operate by the mantra of thinking critically, executing, and taking ownership of our decisions.</p>
    </div>
    <div class="norm" style="left:358px;top:823px">
      <h2>Stay 1StepAhead:</h2>
      <p>We strive to stay one step ahead, anticipating needs and proactively addressing challenges.</p>
    </div>
    <div class="norm" style="left:296px;top:909px">
      <h2>Creating Healthy Environments:</h2>
      <p>We are committed to establishing comfortable environments where our clients can thrive and be productive.</p>
    </div>
    <div class="norm" style="left:204px;top:979px">
      <h2>Setting Higher Standards:</h2>
      <p>We aim to elevate the standards of the mechanical industry by educating both our customers and ourselves, constantly raising the bar.</p>
    </div>

    <div class="footer-bar"></div>
    <svg class="footer-accent" width="773" height="1085" viewBox="0 0 773 1085">
      <path d="M524 1061 L512 1085 H518 L530 1061z" fill="var(--white)"/>
      <path d="M547 1052 Q550 1051 773 1051 V1085 H529z" fill="var(--gold)"/>
    </svg>
  </div>
</div>
</body>
</html>
```